German tourism publishing house needs for international wellness hotel guide

We are planning as a print catalog. For this hotel directory we need a meaningful and appealing cover. The contents, a wide offer of wellness hotels should be recognizable at first sight. The title should make you want to go on a wellness holiday. The target group of the book are customers. We are looking forward to your next visit! The title "Wellness Hotels" should be larger on the cover written. The "Ruvaro logo" should be smaller on the cover. Please integrate the Internet address www.ruvaro-example.de small on the cover

Industry/Entity Type

Tourism

Font styles to use
Serif
Sans Serif

Colors
0355a3
ffffff
85acd3

Requirements
Must have
• We are looking forward to your next visit! The title "Wellness Hotels" should be larger on the cover written. The "Ruvaro logo" should be smaller on the cover.
Nice to have
• Please integrate the Internet address www.ruvaro-example.de small on the cover

```html
<!DOCTYPE html>
<html lang="en">
<head>
<meta charset="utf-8">
<title>Wellness Hotels – Catalog Cover</title>
<link rel="stylesheet" href="https://fonts.googleapis.com/css2?family=Cinzel:wght@400&family=Crimson+Text:wght@400&display=swap">
<style>
  :root {
    --brand-blue: #0355a3;
    --deep-blue: #0a3f86;
    --soft-blue: #85acd3;
    --white: #ffffff;
    --stage: #ececec;
  }
  * { box-sizing: border-box; margin: 0; padding: 0; }
  html, body { width: 1200px; height: 800px; overflow: hidden; }
  body {
    background: radial-gradient(ellipse at center, #fafafa 0%, var(--stage) 100%);
    font-family: "Crimson Text", Georgia, serif;
    position: relative;
  }
  .spread {
    position: absolute; left: 180px; top: 100px;
    width: 840px; height: 600px;
    display: flex;
    box-shadow: 0 14px 30px rgba(0,0,0,0.18);
  }
  /* Back cover */
  .back-cover {
    width: 400px; height: 600px;
    background:
      linear-gradient(180deg, rgba(26,95,174,0.92) 0%, rgba(3,85,163,0.9) 45%, rgba(10,63,134,0.95) 100%),
      linear-gradient(90deg, #2c6bb5 0%, #0d4a94 50%, #3a78bf 100%);
    color: var(--white);
    position: relative;
    padding: 38px 34px 0 34px;
  }
  .back-cover p {
    font-size: 13.4px; line-height: 1.13;
    text-align: justify; hyphens: auto;
    margin-bottom: 18px;
  }
  .back-brand {
    position: absolute; left: 0; right: 0; bottom: 48px;
    text-align: center;
  }
  /* Spine */
  .spine {
    width: 40px; height: 600px;
    background: linear-gradient(90deg, var(--deep-blue), var(--brand-blue) 50%, var(--deep-blue));
    position: relative;
    color: var(--white);
  }
  .spine-title {
    position: absolute; left: 50%; top: 40px;
    transform: translateX(-50%) rotate(180deg);
    writing-mode: vertical-rl;
    font-family: "Cinzel", "Times New Roman", serif;
    font-weight: 400;
    font-size: 20px; letter-spacing: 2px;
  }
  .spine-brand {
    position: absolute; left: 50%; bottom: 22px;
    transform: translateX(-50%) rotate(180deg);
    writing-mode: vertical-rl;
    font-size: 11px;
  }
  /* Front cover */
  .front-cover {
    width: 400px; height: 600px;
    position: relative; overflow: hidden;
    background: linear-gradient(180deg, var(--white) 0%, var(--white) 60%, var(--soft-blue) 82%, var(--brand-blue) 100%);
  }
  .cover-title {
    position: absolute; top: 20px; left: 0; right: 0;
    text-align: center;
    font-family: "Cinzel", "Times New Roman", serif;
    font-weight: 400;
    color: var(--brand-blue);
    line-height: 0.98; z-index: 3;
  }
  .cover-title .line-1 { display: block; font-size: 56px; letter-spacing: 0.5px; }
  .cover-title .line-2 { display: block; font-size: 46px; letter-spacing: 4px; }
  .photo { position: absolute; }
  .photo-lounge   { left: 0;    top: 150px; width: 78px;  height: 86px;
                    background: linear-gradient(160deg, #efe8d8 0%, #c9b98e 55%, #8d8a5a 100%); }
  .photo-pool     { left: 90px; top: 120px; width: 195px; height: 118px;
                    background: linear-gradient(180deg, rgba(255,255,255,0.95) 0%, #e3dcd6 45%, #c7b8ab 100%); }
  .photo-sauna    { left: 296px; top: 150px; width: 104px; height: 126px;
                    background: linear-gradient(180deg, #f0ece8 0%, #cdb6a2 55%, #a6826a 100%); }
  .photo-spa-room { left: 0;    top: 248px; width: 285px; height: 196px;
                    background: linear-gradient(180deg, #d8d1cb 0%, #b4aaa3 35%, #8c8d94 65%, #6d7a8e 100%); }
  .photo-relax    { left: 296px; top: 288px; width: 104px; height: 118px;
                    background: linear-gradient(180deg, #f1f3f7 0%, #c3c6d6 55%, #8d93ad 100%); }
  .photo-hallway  { left: 0;    top: 456px; width: 285px; height: 144px;
                    background: linear-gradient(180deg, #b7cde6 0%, #6f98c9 45%, var(--brand-blue) 100%); }
  .photo-town     { left: 296px; top: 418px; width: 104px; height: 182px;
                    background: linear-gradient(180deg, #c1d6ee 0%, #8fb0d8 45%, #4f6f9e 100%); }
  .front-brand {
    position: absolute; left: 0; width: 285px; top: 356px;
    text-align: center; z-index: 3;
  }
  .brand-name {
    font-family: "Crimson Text", Georgia, serif;
    color: var(--white);
    font-weight: 400;
    display: inline-flex; align-items: center; gap: 8px;
  }
  .brand-name .dot {
    width: 11px; height: 11px; border-radius: 50%;
    background: var(--white); display: inline-block;
  }
  .front-brand .brand-name { font-size: 48px; line-height: 1; }
  .back-brand .brand-name { font-size: 44px; line-height: 1; }
  .web-address {
    position: absolute; left: 0; width: 285px; bottom: 14px;
    text-align: center; z-index: 3;
    font-family: "Crimson Text", Georgia, serif;
    font-size: 13px; letter-spacing: 0.5px;
    color: var(--white);
  }
</style>
</head>
<body>
  <main class="spread">
    <section class="back-cover">
      <p>Lorem ipsum dolor sit amet, consectetur adipiscing elit. Nullam feugiat neque in varius molestie. Pellentesque rhoncus scelerisque molestie. Nulla consectetur libero ut ex pharetra ultricies. Mauris id tempor augue. Suspendisse facilisis purus ac velit dictum gravida. Phasellus neque enim, fringilla sit amet mollis et, aliquet sed elit. Curabitur consectetur accumsan sem, a fringilla arcu euismod ut. Nunc eget euismod arcu. Nulla suscipit tempor mauris quis posuere. Nulla a lectus ac diam posuere venenatis. Nam faucibus pretium tincidunt. Nunc eu mi lectus. Nunc at turpis et nibh sodales malesuada. Nulla ipsum augue, blandit nec convallis ornare, consectetur a lacus. Proin vel feugiat risus.</p>
      <p>Pellentesque auctor libero ac turpis euismod viverra. Etiam aliquam vel nunc ut vehicula. Sed nec hendrerit lacus. Suspendisse interdum volutpat magna non dapibus. Morbi malesuada vehicula leo, ac malesuada felis ultrices laoreet. Cras ornare fermentum urna, sit amet dapibus tortor tristique in. Sed vitae ex ullamcorper, sodales est sit amet, vestibulum massa. Duis dapibus dolor sit amet neque gravida efficitur. Fusce vel volutpat felis. Nunc eget pretium urna, vitae accumsan leo. Ut quis ante bibendum, maximus nulla in, aliquet arcu. Aliquam et imperdiet ligula. Nullam blandit erat quis tellus vulputate feugiat. Donec non imperdiet urna. Praesent aliquam mattis odio, vel volutpat lacus egestas sit amet. Integer tristique ipsum vel mi accumsan convallis.</p>
      <div class="back-brand"><span class="brand-name"><span class="dot"></span>Ruvaro</span></div>
    </section>

    <section class="spine">
      <span class="spine-title">WELLNESS HOTELS</span>
      <span class="spine-brand">Ruvaro</span>
    </section>

    <section class="front-cover">
      <h1 class="cover-title"><span class="line-1">WELLNESS</span><span class="line-2">HOTELS</span></h1>
      <div class="photo photo-lounge" role="img" aria-label="Hotel lounge with plants"></div>
      <div class="photo photo-pool" role="img" aria-label="Couple relaxing in a candlelit whirlpool"></div>
      <div class="photo photo-sauna" role="img" aria-label="Wooden sauna interior"></div>
      <div class="photo photo-spa-room" role="img" aria-label="Spa relaxation room with lake view window"></div>
      <div class="photo photo-relax" role="img" aria-label="Bright relaxation area with loungers"></div>
      <div class="photo photo-hallway" role="img" aria-label="Spa hallway with wooden door"></div>
      <div class="photo photo-town" role="img" aria-label="Half-timbered hotel building"></div>
      <div class="front-brand"><span class="brand-name"><span class="dot"></span>Ruvaro</span></div>
      <div class="web-address">www.ruvaro-example.de</div>
    </section>
  </main>
</body>
</html>
```